Fall Postcard Mailers for Roofing Company

We need a postcard for a mailer designed for ShingleGuide. ShingleGuide is professional and personable. Unlike most roofing companies our Advisors are Non-Commissioned so they provide Unbiased advise. Our Advisors provide an In-depth Roof Analysis for each home. This is much like a home inspection report with pictures and description.

Homeowner demographics are upscale neighborhoods with homeowners over 40 years old with properties over $250,000. All pictures and colors can be pulled from www.ShingleGuideMi.example and our Facebook page https://www.facebook.com/MyShingleGuide/. We are based in Plymouth, Mi.

I've attached some of our other marketing materials.

Target Market(s)

Homeowners
40 years old and above
Home value over $250,000

Industry/Entity Type

Roofing

Requirements
Must have
• Space designed for mail printing on front
• Add a three discount coupons
• -Up to $2,500 off Roof Replacement
• -FREE Roof Analysis up to $500 value
• -Up to $100 off Roof Repair
• Non-Commissioned Advisors=Unbiased Guidance
• Financing Available
• Company colors:
• G: C-0 M-0 Y-0 K-80
• O: C-0 M-54 Y-95 K-0
Nice to have
• We are trying to drive action: Calls, website visits, inquiries.
• Personable and professional.
Should not have
• Too much open space.

```html
<!DOCTYPE html>
<html lang="en">
<head>
<meta charset="utf-8">
<title>ShingleGuide Fall Postcard Mailer</title>
<link rel="stylesheet" href="https://fonts.googleapis.com/css2?family=Exo+2:wght@400;600;700;800&family=Roboto+Condensed:wght@400;700&family=Open+Sans:wght@400;600&display=swap">
<style>
:root{
  --orange:#f58a1f;
  --gray:#58595b;
  --dark:#232323;
  --ink:#4a4a4a;
  --white:#ffffff;
  --page:#d9d9d9;
}
*{margin:0;padding:0;box-sizing:border-box}
html,body{width:809px;height:1200px;overflow:hidden;background:var(--page)}
body{position:relative;font-family:"Exo 2",sans-serif;color:var(--ink)}
.card{position:absolute;left:37px;width:675px;background:var(--white);overflow:hidden}
.card-front{top:38px;height:524px}
.card-back{top:621px;height:522px}
.card svg.shapes{position:absolute;inset:0}
.abs{position:absolute;white-space:nowrap}

/* front */
.brand{left:24px;top:26px;font-size:50px;font-weight:600;color:var(--orange);letter-spacing:-.5px;display:flex;align-items:center;gap:10px}
.brand-mark{width:14px;height:14px;background:var(--gray)}
.tagline{left:20px;top:98px;font-size:22px;line-height:26px;font-weight:400;color:var(--ink)}
.headline{left:20px;top:152px;font-size:27px;font-weight:700;color:var(--orange);letter-spacing:.3px}
.coupon{position:absolute;left:18px;border:1px dashed rgba(255,255,255,.55);border-radius:6px;display:flex;align-items:center;white-space:nowrap}
.coupon-replace{top:212px;width:364px;height:54px}
.coupon-analysis{top:304px;width:350px;height:50px}
.coupon-repair{top:393px;width:333px;height:54px}
.up-to{font-size:17px;color:var(--white);margin:0 4px 0 6px}
.amount{font-weight:800;font-size:44px;color:var(--orange);letter-spacing:-1px;line-height:1}
.off-tag{background:var(--orange);color:var(--white);font-weight:700;font-size:14px;padding:1px 3px;margin:10px 8px 0 2px}
.coupon-label{font-weight:700;font-size:18px;line-height:18px;color:var(--white);text-transform:uppercase}
.free{display:flex;flex-direction:column;margin:0 8px 0 14px;color:var(--white)}
.free b{font-size:36px;font-weight:800;line-height:32px}
.free span{font-size:11.5px;font-weight:600;letter-spacing:.2px}
.rotated{writing-mode:vertical-rl;transform:rotate(180deg);white-space:nowrap;font-size:15px;line-height:15px;color:var(--gray);margin:0 6px 0 2px}
.amount-dark{font-weight:800;font-size:44px;color:var(--gray);letter-spacing:-1px;line-height:1}
.off-value{background:var(--gray);color:var(--white);font-weight:700;font-size:16px;padding:1px 4px;margin:8px 0 0 3px}
.connect{left:17px;top:466px;font-family:"Open Sans",sans-serif;font-size:12.5px;color:var(--dark)}
.connect em{font-style:normal;color:var(--orange)}
.social{left:17px;top:490px;display:flex;align-items:center;gap:6px;font-family:"Open Sans",sans-serif;font-size:12px;color:var(--ink)}
.dot{width:19px;height:19px;border-radius:50%;background:var(--orange)}
.expert{font-family:"Roboto Condensed",sans-serif;font-weight:700;font-size:16px;color:var(--orange);letter-spacing:.2px}
.phone{font-family:"Roboto Condensed",sans-serif;font-weight:700;font-size:38px;color:var(--white);letter-spacing:-.3px;line-height:1}
.phone i{font-style:normal;color:var(--orange);font-size:28px;margin-right:8px}
.visit{left:555px;top:476px;background:var(--white);border-radius:6px;padding:0 6px;font-family:"Open Sans",sans-serif;font-size:11px;color:var(--dark)}
.web{font-family:"Open Sans",sans-serif;font-weight:600;letter-spacing:.3px;display:flex;align-items:center;gap:7px}

/* back */
.back-head{left:0;width:320px;text-align:center;font-weight:700;text-transform:uppercase}
.nca{top:14px;font-size:27px;line-height:30px;color:var(--white);letter-spacing:.8px}
.unbiased{top:76px;font-size:26px;color:var(--orange);letter-spacing:.8px}
.financing{position:absolute;left:34px;top:114px;width:252px;height:76px;border:1px dashed var(--orange);border-radius:6px;text-align:center;font-weight:800;font-size:35px;line-height:34px;color:#dcdcdc;letter-spacing:1.5px;padding-top:4px;text-transform:uppercase}
.service{display:flex;align-items:center;gap:20px;font-weight:600;color:var(--white)}
.service .label{font-size:19px;line-height:23px}
.service em{font-style:normal;color:var(--orange)}
.divider{position:absolute;left:93px;width:88px;height:1px;background:var(--orange)}
.brand-back{left:16px;top:449px;font-size:40px;font-weight:600;color:var(--orange);display:flex;align-items:center;gap:8px}
.stamp{position:absolute;left:550px;top:21px;width:106px;height:133px;border:1px solid #9a9a9a;border-radius:8px}
.address-line{position:absolute;left:411px;width:246px;height:1px;background:#9a9a9a}
</style>
</head>
<body>

<section class="card card-front" aria-label="Postcard front">
  <svg class="shapes" width="675" height="524" viewBox="0 0 675 524">
    <defs>
      <linearGradient id="houseTones" x1="0" y1="0" x2="0" y2="1">
        <stop offset="0" stop-color="#9fc3e6"/>
        <stop offset=".3" stop-color="#d9d6d0"/>
        <stop offset=".62" stop-color="#7a4a3c"/>
        <stop offset=".78" stop-color="#5c7d3a"/>
        <stop offset="1" stop-color="#6a9a3a"/>
      </linearGradient>
    </defs>
    <rect x="0" y="207" width="430" height="63" fill="var(--gray)"/>
    <polygon points="180,270 198,270 189,280" fill="var(--gray)"/>
    <rect x="0" y="298" width="430" height="61" fill="var(--orange)"/>
    <polygon points="180,359 198,359 189,369" fill="var(--orange)"/>
    <rect x="0" y="388" width="430" height="62" fill="var(--gray)"/>
    <polygon points="180,450 198,450 189,460" fill="var(--gray)"/>
    <path d="M396 0 H675 V524 H312 C422 330 432 120 396 0Z" fill="var(--orange)"/>
    <path d="M378 0 H398 C434 120 424 330 314 524 H292 C402 330 412 120 378 0Z" fill="var(--gray)"/>
    <path d="M420 0 H675 V400 H392 C432 280 442 120 420 0Z" fill="url(#houseTones)"/>
    <path d="M392 402 H675 V470 H350 C368 448 382 426 392 402Z" fill="var(--dark)"/>
  </svg>
  <div role="img" aria-label="Photo of a brick two-storey home with a roofing advisor on the roof" class="abs" style="left:430px;top:0;width:245px;height:400px"></div>

  <div class="abs brand"><span>ShingleGuide</span><span class="brand-mark"></span></div>
  <p class="abs tagline">Professional Advice Tailored<br>to Your Roofing Needs</p>
  <h1 class="abs headline">LET US MEET YOUR ROOF</h1>
  <svg class="abs" style="left:20px;top:188px" width="92" height="3"><rect width="92" height="3" fill="var(--orange)"/></svg>

  <div class="coupon coupon-replace">
    <span class="up-to">Up to</span><span class="amount">$2,500</span><span class="off-tag">OFF</span>
    <span class="coupon-label">Roof<br>Replacement</span>
  </div>
  <div class="coupon coupon-analysis" style="border-color:rgba(88,89,91,.6)">
    <span class="free"><b>FREE</b><span>ROOF ANALYSIS</span></span>
    <span class="rotated">up to</span>
    <span class="amount-dark">$500</span><span class="off-value">OFF VALUE</span>
  </div>
  <div class="coupon coupon-repair">
    <span class="up-to" style="margin-left:28px">Up to</span><span class="amount">$100</span><span class="off-tag">OFF</span>
    <span class="coupon-label" style="margin-left:14px">Roof<br>Repair</span>
  </div>

  <p class="abs connect">Connect <em>With Us:</em></p>
  <div class="abs social"><span class="dot"></span><span>MyShingleGuide/</span><span class="dot" style="margin-left:6px"></span></div>

  <p class="abs expert" style="left:404px;top:409px">SPEAK WITH A ROOFING EXPERT:</p>
  <p class="abs phone" style="left:405px;top:429px"><i>&gt;</i>555-MI-Guides</p>
  <span class="abs visit">Visit our Website</span>
  <p class="abs web" style="left:384px;top:493px;font-size:16px;color:var(--white)">
    <svg width="15" height="15" viewBox="0 0 16 16" fill="none" stroke="#fff" stroke-width="1.3"><circle cx="8" cy="8" r="7"/><ellipse cx="8" cy="8" rx="3" ry="7"/><path d="M1 8h14"/></svg>
    www.shingleguidemi.example
  </p>
</section>

<section class="card card-back" aria-label="Postcard back">
  <svg class="shapes" width="675" height="522" viewBox="0 0 675 522">
    <defs>
      <linearGradient id="darkTones" x1="0" y1="0" x2="0" y2="1">
        <stop offset="0" stop-color="#2d2d2d"/>
        <stop offset=".5" stop-color="#3a3836"/>
        <stop offset="1" stop-color="#262626"/>
      </linearGradient>
    </defs>
    <path d="M319 0 C372 120 385 300 322 522 H340 C400 300 388 120 333 0Z" fill="var(--orange)"/>
    <path d="M0 0 H312 C362 120 372 300 310 522 H0Z" fill="url(#darkTones)"/>
    <path d="M0 374 H346 C343 395 338 415 332 435 H0Z" fill="#141414" opacity=".85"/>
  </svg>
  <div role="img" aria-label="Dark photo of a roofing advisor inspecting shingles" class="abs" style="left:0;top:0;width:312px;height:522px"></div>

  <p class="abs back-head nca">Non-Commissioned<br>Advisors</p>
  <p class="abs back-head unbiased">Unbiased Guidance</p>
  <div class="financing">Financing<br>Available</div>

  <div class="abs service" style="left:36px;top:210px">
    <svg width="40" height="44" viewBox="0 0 40 44" fill="none" stroke-width="3"><path d="M4 18 L20 4 L36 18" stroke="#fff"/><circle cx="20" cy="26" r="7" stroke="var(--orange)"/><path d="M25 31 L31 38" stroke="var(--orange)"/></svg>
    <span class="label">Analysis &amp; No-Leak<br><em>Certification</em></span>
  </div>
  <span class="divider" style="top:267px"></span>
  <div class="abs service" style="left:36px;top:278px">
    <svg width="40" height="36" viewBox="0 0 40 36"><path d="M4 18 L20 4 L36 18 V34 H4Z" fill="#fff"/><rect x="16" y="22" width="8" height="12" fill="var(--dark)"/><circle cx="20" cy="12" r="5" fill="var(--orange)"/></svg>
    <span class="label">LEAK &amp; DAMAGE <em>REPAIR</em></span>
  </div>
  <span class="divider" style="top:315px"></span>
  <div class="abs service" style="left:36px;top:326px">
    <svg width="40" height="36" viewBox="0 0 40 36"><path d="M2 16 L20 6 L38 16Z" fill="#fff"/><rect x="6" y="18" width="28" height="16" fill="var(--orange)"/><rect x="12" y="22" width="5" height="6" fill="#fff"/><rect x="23" y="22" width="5" height="6" fill="#fff"/></svg>
    <span class="label">REPLACEMENT</span>
  </div>

  <p class="abs expert" style="left:17px;top:380px">SPEAK WITH A ROOFING EXPERT:</p>
  <p class="abs phone" style="left:17px;top:398px"><i>&gt;</i>555-MI-Guides</p>
  <div class="abs brand-back"><span>ShingleGuide</span><span class="brand-mark" style="width:11px;height:11px;background:#bdbdbd"></span></div>
  <p class="abs web" style="left:17px;top:496px;font-size:15.5px;color:#e6e6e6;font-weight:400">
    <svg width="13" height="13" viewBox="0 0 16 16" fill="none" stroke="var(--orange)" stroke-width="1.4"><circle cx="8" cy="8" r="7"/><ellipse cx="8" cy="8" rx="3" ry="7"/><path d="M1 8h14"/></svg>
    www.shingleguidemi.example
  </p>

  <div class="stamp"></div>
  <span class="address-line" style="top:235px"></span>
  <span class="address-line" style="top:291px"></span>
  <span class="address-line" style="top:350px"></span>
  <span class="address-line" style="top:405px"></span>
</section>

</body>
</html>
```